Marla's Glimmerbox Shower Banner

I need a banner design for a bridal shower. The banner size is 4 feet by 8 feet, so the artwork needs to be appropriately vertical (4'x8') I would like the design to be a fake glimmerbox post with the attached photo and hashtags.
Please add emoji's to the hashtags. hearts, and engagement ring, a tropical drink, a flip flop (if there is one.)

```html
<!DOCTYPE html>
<html lang="en">
<head>
<meta charset="utf-8">
<title>Marla's Shower – Glimmerbox Post Banner</title>
<link rel="stylesheet" href="https://fonts.googleapis.com/css2?family=Open+Sans:wght@400;600&display=swap">
<style>
  :root {
    --lime: #80e01c;
    --white: #ffffff;
    --ink: #1c1c1c;
    --muted: #b9b9b9;
    --tag: #2f74d0;
    --like: #e0262b;
    --nav-dark: #1d1d1d;
    --nav-mid: #2c2c2c;
    --nav-icon: #9a9a9a;
    --photo-sky: #d9d6d4;
    --photo-stand: #c23a4c;
    --photo-shirt: #a52636;
    --photo-deep: #7c1c28;
  }
  * { box-sizing: border-box; margin: 0; padding: 0; }
  html, body { width: 725px; height: 1200px; overflow: hidden; background: var(--white); }
  body { font-family: "Open Sans", Arial, sans-serif; color: var(--ink); }
  .banner { position: relative; width: 725px; height: 1200px; background: var(--white); }

  .app-bar { position: absolute; top: 0; left: 0; width: 100%; height: 115px; background: var(--lime); }
  .app-name { position: absolute; left: 0; right: 0; top: 24px; text-align: center; color: var(--white); font-size: 46px; font-weight: 600; line-height: 1.2; }
  .inbox-icon { position: absolute; right: 24px; top: 35px; width: 52px; height: 44px; }

  .post-header { position: absolute; top: 130px; left: 0; width: 100%; height: 70px; }
  .avatar { position: absolute; left: 28px; top: 2px; width: 68px; height: 68px; }
  .account-name { position: absolute; left: 112px; top: 18px; font-size: 23px; letter-spacing: 0.5px; }
  .post-time { position: absolute; right: 22px; top: 16px; display: flex; align-items: center; gap: 4px; color: var(--muted); font-size: 22px; font-weight: 600; }
  .post-time svg { width: 22px; height: 22px; }

  .post-photo { position: absolute; top: 213px; left: 0; width: 100%; height: 662px;
    background:
      radial-gradient(ellipse 60% 50% at 28% 55%, rgba(222,170,150,0.55), rgba(222,170,150,0) 70%),
      radial-gradient(ellipse 40% 40% at 78% 75%, rgba(220,168,148,0.45), rgba(220,168,148,0) 70%),
      linear-gradient(180deg, var(--photo-sky) 0%, var(--photo-stand) 32%, var(--photo-shirt) 68%, var(--photo-deep) 100%); }

  .action-row { position: absolute; top: 902px; left: 0; width: 100%; height: 40px; }
  .action-row svg { position: absolute; top: 0; width: 38px; height: 38px; }
  .icon-like { left: 34px; }
  .icon-comment { left: 86px; }
  .icon-share { left: 138px; }
  .icon-save { right: 34px; }

  .like-count { position: absolute; top: 954px; left: 34px; font-size: 22px; display: flex; align-items: center; gap: 6px; }
  .like-count svg { width: 20px; height: 20px; }

  .caption { position: absolute; top: 986px; left: 42px; right: 12px; font-size: 20.5px; line-height: 28px; white-space: nowrap; }
  .caption .user { color: var(--ink); }
  .caption .tags { color: var(--tag); }
  .caption .emoji { font-size: 19px; letter-spacing: 1px; }

  .nav-bar { position: absolute; bottom: 0; left: 0; width: 100%; height: 96px; display: flex; }
  .nav-item { flex: 1; display: flex; align-items: center; justify-content: center; background: var(--nav-mid); }
  .nav-item.is-home { background: var(--nav-dark); }
  .nav-item.is-camera { background: var(--lime); }
  .nav-item svg { width: 50px; height: 50px; }
</style>
</head>
<body>
<main class="banner">

  <header class="app-bar">
    <div class="app-name">Glimmerbox</div>
    <svg class="inbox-icon" viewBox="0 0 52 44" aria-hidden="true">
      <path d="M6 4h40l6 18v18a4 4 0 0 1-4 4H4a4 4 0 0 1-4-4V22z" fill="var(--white)"/>
      <path d="M8 24h11l3 6h8l3-6h11" fill="none" stroke="var(--lime)" stroke-width="3"/>
      <path d="M10 10h32l4 12H6z" fill="var(--lime)"/>
    </svg>
  </header>

  <section class="post-header">
    <svg class="avatar" viewBox="0 0 68 68" aria-hidden="true">
      <circle cx="34" cy="34" r="34" fill="var(--ink)"/>
      <circle cx="34" cy="28" r="15" fill="var(--white)"/>
      <path d="M10 62c4-14 14-20 24-20s20 6 24 20z" fill="var(--white)"/>
    </svg>
    <div class="account-name">Marla's Shower</div>
    <div class="post-time">
      <svg viewBox="0 0 22 22" aria-hidden="true"><circle cx="11" cy="11" r="10" fill="var(--muted)"/><path d="M11 5v6h5" stroke="var(--white)" stroke-width="2.4" fill="none"/></svg>
      <span>2m</span>
    </div>
  </section>

  <div class="post-photo" role="img" aria-label="Photo of the engaged couple smiling together in matching red football jerseys inside a stadium with red stands"></div>

  <section class="action-row">
    <svg class="icon-like" viewBox="0 0 24 24" aria-hidden="true"><path d="M12 21s-9-6-9-12a5 5 0 0 1 9-3 5 5 0 0 1 9 3c0 6-9 12-9 12z" fill="var(--like)"/></svg>
    <svg class="icon-comment" viewBox="0 0 24 24" aria-hidden="true"><path d="M12 3a9 9 0 1 0 4.5 16.8L21 21l-1.3-4.3A9 9 0 0 0 12 3z" fill="none" stroke="var(--ink)" stroke-width="2"/></svg>
    <svg class="icon-share" viewBox="0 0 24 24" aria-hidden="true"><path d="M2 4l20 0-10 17-2-9z M10 12L22 4" fill="none" stroke="var(--ink)" stroke-width="2" stroke-linejoin="round"/></svg>
    <svg class="icon-save" viewBox="0 0 24 24" aria-hidden="true"><path d="M5 2h14v20l-7-7-7 7z" fill="none" stroke="var(--ink)" stroke-width="2" stroke-linejoin="round"/></svg>
  </section>

  <div class="like-count">
    <svg viewBox="0 0 24 24" aria-hidden="true"><path d="M12 21s-9-6-9-12a5 5 0 0 1 9-3 5 5 0 0 1 9 3c0 6-9 12-9 12z" fill="var(--ink)"/></svg>
    <span>81,118 likes</span>
  </div>

  <p class="caption">
    <span class="user">marla</span> <span class="tags">#marla'sshower #summerwedding #happilyeverafter</span><br>
    <span class="tags">#futbolfun #marlaanddanny2018 #dannyscored! #marriagegoals</span><br>
    <span class="tags">#trueloveforever #beantownbliss #goherons! #harborcollege'13</span><br>
    <span class="tags">#sportycouple #playtogetherstaytogether</span> <span class="emoji">❤️💍🍹🩴</span>
  </p>

  <nav class="nav-bar">
    <div class="nav-item is-home">
      <svg viewBox="0 0 50 50" aria-hidden="true"><path d="M25 6L4 26h6v18h11V33h8v11h11V26h6z" fill="var(--white)"/></svg>
    </div>
    <div class="nav-item">
      <svg viewBox="0 0 50 50" aria-hidden="true"><circle cx="21" cy="21" r="13" fill="none" stroke="var(--nav-icon)" stroke-width="4"/><path d="M31 31l12 12" stroke="var(--nav-icon)" stroke-width="5" stroke-linecap="round"/></svg>
    </div>
    <div class="nav-item is-camera">
      <svg viewBox="0 0 50 50" aria-hidden="true"><rect x="3" y="3" width="44" height="44" rx="8" fill="var(--white)"/><circle cx="25" cy="25" r="12" fill="none" stroke="var(--lime)" stroke-width="3"/></svg>
    </div>
    <div class="nav-item">
      <svg viewBox="0 0 50 50" aria-hidden="true"><path d="M25 4a20 20 0 1 0 9 38l8 3-2-8A20 20 0 0 0 25 4z" fill="var(--nav-icon)"/><path d="M25 35s-10-6-10-12a5 5 0 0 1 10-2 5 5 0 0 1 10 2c0 6-10 12-10 12z" fill="var(--nav-mid)"/></svg>
    </div>
    <div class="nav-item">
      <svg viewBox="0 0 50 50" aria-hidden="true"><circle cx="25" cy="16" r="10" fill="var(--nav-icon)"/><path d="M6 46c2-12 10-18 19-18s17 6 19 18z" fill="var(--nav-icon)"/></svg>
    </div>
  </nav>

</main>
</body>
</html>
```